PSD Designs needed to give to my Developer

Hello, I need PSD files to give to my programmer for the creation of my new website. The website is for ZORVA lane, a new clothing company based in Chicago, IL. We sell womens, mens and kids fashion. We specialize in jackets, outerwear and sweaters, but we sell clothing from every category, I have someone working on the logo, so I can't include it for reference. However, I have included 2 reference sites as well as a PDF of how the 2 reference sites could be merged together. The main company color should be blue (hence the name ZORVA lane), and the overall feel of the site should be FUN. It should communicate: This is where you want to shop if you want a FUN, HAPPY experience. I need the Home Page file designed very quickly. Whoever is awarded this job will immediately continue working with me to design the other 8 pages. I will pay for all pages. The amount I am offering is for this one page only, and I will pay you additional to design all other 8 pages. Thank you for your time and I will be picking the best design so that we can immediately build a great relationship and work through the rest of the project.

Industry/Entity Type

Apparel Store

Number of Pages Required

1 page

Font styles to use
Sans Serif

Colors
33a6d7
0492cd
ffffff

Requirements
Must have
• I have included all notes in the project description so please check there. My project must communicate: Fun and Happy Design. Even tho I have chosen a few variations of blue below, I still want the designer to incorporate other colors as necessary to acheive the desired look.
Should not have
• It should have a boring, childish feel

```html
<!DOCTYPE html>
<html lang="en">
<head>
<meta charset="utf-8">
<title>ZORVA lane — Home</title>
<link href="https://fonts.googleapis.com/css2?family=Raleway:wght@400;500;600;700;800&display=swap" rel="stylesheet">
<style>
  :root{
    --blue:#137dc5;
    --blue-deep:#0f6fb0;
    --topbar:#e8e8e8;
    --hero-bg:#f3f2f0;
    --ink:#1c1c1c;
    --white:#ffffff;
    --footer:#1f1f1f;
  }
  *{box-sizing:border-box;margin:0;padding:0}
  html,body{width:1173px;height:1200px;overflow:hidden;background:var(--white)}
  body{position:relative;font-family:'Raleway',sans-serif;color:var(--ink)}

  .topbar{position:absolute;left:0;top:0;width:1173px;height:49px;background:var(--topbar)}
  .topbar__promo{position:absolute;left:96px;top:16px;font-size:13px;font-weight:600;color:#2a2a2a}
  .topbar__arrow{position:absolute;left:930px;top:14px}
  .login-btn{position:absolute;left:987px;top:9px;width:88px;height:30px;border:1.5px solid #2a2a2a;border-radius:15px;
    display:flex;align-items:center;justify-content:center;gap:7px;font-size:13px;font-weight:600;color:#2a2a2a}

  .mainnav{position:absolute;left:0;top:49px;width:1173px;height:69px;background:var(--blue)}
  .mainnav__links{position:absolute;left:96px;top:0;height:69px;display:flex;align-items:center;list-style:none}
  .mainnav__links li{font-size:12.5px;font-weight:600;color:var(--white);margin-right:48px;position:relative;height:69px;line-height:69px}
  .mainnav__links li.is-active::after{content:"";position:absolute;left:1px;right:0;bottom:0;height:3px;background:var(--white)}
  .brand{position:absolute;right:98px;top:16px;font-size:30px;font-weight:600;color:var(--white);letter-spacing:.5px}

  .hero{position:absolute;left:0;top:118px;width:1173px;height:459px;background:var(--hero-bg);overflow:hidden}
  .hero__photo{position:absolute;left:20px;top:0;width:390px;height:459px;
    background:radial-gradient(ellipse 40% 55% at 50% 55%, #a8743c 0%, #b98a55 35%, rgba(230,226,220,0) 75%),
    linear-gradient(180deg,#efeeec,#e9e7e3)}
  .promo-frame{position:absolute;left:367px;top:75px;width:581px;height:310px;border:6px solid var(--blue);
    display:flex;flex-direction:column;align-items:center;justify-content:center;text-align:center;padding-bottom:18px}
  .promo-frame__lead{font-size:38px;font-weight:800;letter-spacing:.5px;line-height:1.2}
  .promo-frame__body{font-size:42px;font-weight:400;line-height:1.4}
  .promo-frame__body strong{font-weight:800}
  .shop-now{position:absolute;left:341px;top:260px;width:154px;height:154px;border-radius:50%;background:var(--blue);
    display:flex;align-items:center;justify-content:center;color:var(--white);font-size:15px;font-weight:600}
  .shop-now::before{content:"";position:absolute;inset:8px;border-radius:50%;border:2px dotted rgba(255,255,255,.85)}
  .hero__dots{position:absolute;left:550px;top:425px;display:flex;gap:10px}
  .hero__dots span{width:11px;height:11px;border-radius:50%;background:var(--blue);border:2px solid var(--blue)}
  .hero__dots span.is-current{background:transparent}

  .tile{position:absolute;overflow:hidden}
  .tile__label{position:absolute;font-weight:700;line-height:1.15}
  .tile--story{left:0;top:587px;width:463px;height:508px;
    background:radial-gradient(ellipse 45% 40% at 28% 58%,#d9a78e 0%,rgba(217,167,142,0) 70%),
    radial-gradient(ellipse 50% 30% at 20% 95%,#e2456d 0%,rgba(226,69,109,0) 70%),
    linear-gradient(160deg,#f3f1ef 0%,#e6dfe3 55%,#e9c8cf 100%)}
  .tile--story .tile__label{left:176px;top:62px;font-size:49px;color:#262626;font-weight:600}
  .tile--shop{left:473px;top:587px;width:700px;height:249px;
    background:radial-gradient(ellipse 30% 50% at 62% 55%,#8f7b6f 0%,rgba(143,123,111,0) 70%),
    linear-gradient(90deg,#1e2a3a 0%,#3a4658 40%,#7d8795 70%,#c9ced6 100%)}
  .tile--shop .tile__label{left:95px;top:98px;font-size:49px;color:var(--white);text-shadow:0 2px 6px rgba(0,0,0,.35)}
  .tile--movement{left:473px;top:846px;width:700px;height:249px;
    background:radial-gradient(ellipse 30% 40% at 62% 60%,#1f78d1 0%,rgba(31,120,209,0) 70%),
    linear-gradient(180deg,#2f4a46 0%,#4f6e49 45%,#8aa255 75%,#a6b86a 100%)}
  .tile--movement .tile__label{left:31px;top:84px;font-size:34px;color:var(--white);text-shadow:0 2px 6px rgba(0,0,0,.35)}

  .footer{position:absolute;left:0;top:1103px;width:1173px;height:97px;background:var(--footer);color:#f0f0f0;text-align:center;font-size:13px}
  .footer__copy{position:absolute;left:0;right:0;top:27px}
  .footer__links{position:absolute;left:0;right:0;top:54px}
</style>
</head>
<body>
  <header class="topbar">
    <p class="topbar__promo">Pop-up your own ZORVA Boulevard for ONLY $99</p>
    <svg class="topbar__arrow" width="40" height="22" viewBox="0 0 40 22" aria-hidden="true">
      <path d="M2 4 C4 18, 22 18, 36 8" fill="none" stroke="#2a2a2a" stroke-width="1.6"/>
      <path d="M28 6 L37 7 L34 15" fill="none" stroke="#2a2a2a" stroke-width="1.6"/>
    </svg>
    <div class="login-btn">
      <svg width="9" height="11" viewBox="0 0 9 11" aria-hidden="true">
        <path d="M2 5V3.5a2.5 2.5 0 0 1 5 0V5" fill="none" stroke="#2a2a2a" stroke-width="1.4"/>
        <rect x="0.5" y="5" width="8" height="6" rx="1" fill="#2a2a2a"/>
      </svg>
      Login
    </div>
  </header>

  <nav class="mainnav">
    <ul class="mainnav__links">
      <li class="is-active">HOME</li>
      <li>GET TO KNOW US</li>
      <li>WHY ZORVA?</li>
      <li>HOST A POP-UP</li>
      <li>BECOME A STYLIST</li>
    </ul>
    <div class="brand">ZORVA lane</div>
  </nav>

  <section class="hero">
    <div class="hero__photo" role="img" aria-label="Smiling man with glasses wearing a tan suede bomber jacket"></div>
    <div class="promo-frame">
      <p class="promo-frame__lead">LIMITED INVENTORY</p>
      <p class="promo-frame__body">that’s only available for<br><strong>ONE</strong> Week!</p>
    </div>
    <div class="shop-now">SHOP NOW</div>
    <div class="hero__dots"><span></span><span></span><span class="is-current"></span><span></span></div>
  </section>

  <a class="tile tile--story" role="img" aria-label="Happy woman holding shopping bags beside a clothing rack">
    <span class="tile__label">Our Story</span>
  </a>
  <a class="tile tile--shop" role="img" aria-label="Smiling man in a grey blazer inside a clothing store">
    <span class="tile__label">Shop</span>
  </a>
  <a class="tile tile--movement" role="img" aria-label="Two laughing toddlers in blue hoodies sitting outdoors on grass">
    <span class="tile__label">Be Happier,<br>Join the Movement</span>
  </a>

  <footer class="footer">
    <p class="footer__copy">Copyright © 2018 ZORVA lane . All rights reserved.</p>
    <p class="footer__links">Terms &amp; Conditions | Privacy Policy</p>
  </footer>
</body>
</html>
```